Zielgruppe
Ich betreibe eine mobile Hundeschule / Hundetraining. Meine Zielgruppe sind Hundehalter:innen, junge Menschen und jung Gebliebene.
Aufgabenstellung
Das Design soll in erster Linie modern sein, aber auch kompetent und sympathisch wirken. Texte würde ich gerne in Absprache mit dem Designer erstellen.
Ich wünsche mir einen Faltflyer in Standardgröße (ich glaube das heißt DIN lang, 2 mal gefaltet (Wickelfalz), 99x210mm.
IM AMHANG SIND BILDER DER NEUEN HOMEPAGE. DIESE IST NCOH NICHT ONLINE. DAS DESIGN SOLL SICH GERNE AN DEN BILDERN DER HOMEPAGE ORIENTIEREN.

```html
<!DOCTYPE html>
<html lang="de">
<head>
<meta charset="utf-8">
<title>Pfotenwerk Lindental – Faltflyer</title>
<link rel="stylesheet" href="https://fonts.googleapis.com/css2?family=Arvo&family=Open+Sans:wght@400;600;700&display=swap">
<style>
:root{
  --bg:#e9e9eb;
  --paper:#ffffff;
  --sand:#dbd2cc;
  --apricot:#fcd597;
  --brown:#8a6656;
  --ink:#3a3330;
  --placeholder:#e4e4e6;
  --pink:#d6307a;
  --logo-bg:#f8f6f6;
}
*{margin:0;padding:0;box-sizing:border-box}
html,body{width:865px;height:1200px;overflow:hidden;background:var(--bg)}
.stage{position:absolute;left:0;top:0;width:1634px;height:2268px;transform:scale(0.5294);transform-origin:0 0;font-family:"Open Sans",sans-serif;color:var(--ink)}
.sheet{position:absolute;background:var(--paper);box-shadow:6px 8px 10px rgba(0,0,0,.18);overflow:hidden}
.sheet--outer{left:145px;top:119px;width:1348px;height:953px}
.sheet--inner{left:141px;top:1191px;width:1349px;height:954px}
.abs{position:absolute}
.band{position:absolute;background:var(--sand)}
.band--apricot{background:var(--apricot)}
.photo{position:absolute}
.card{position:absolute;background:var(--paper);border-radius:30px;padding:54px 22px 0 23px;font-size:15.6px;line-height:19.5px}
.card--sand{background:var(--sand)}
.label{display:block;font-weight:700;color:var(--brown)}
.slab{font-family:"Arvo",serif;font-weight:400}
.offer{position:absolute;width:248px;background:var(--apricot);border-radius:26px 26px 0 0;text-align:center;padding-top:16px;color:var(--ink)}
.offer__mark{width:30px;height:30px;border-radius:50%;background:#ede6df;border:2px solid #a9a09b;margin:0 auto 14px}
.offer__title{font-size:24px;line-height:30px}
.offer__sub{font-size:16px;margin-top:6px}
.offer__claim{font-size:22px;line-height:26px;margin-top:18px}
.offer__note{font-size:16px;line-height:19.5px;margin-top:8px}
.contact__name{font-size:17px;line-height:20px}
.contact__lines{font-size:16px;line-height:19.5px;margin-top:8px}
.portrait{position:absolute;left:602px;top:96px;width:144px;height:159px;background:var(--placeholder);border-radius:24px;text-align:center;padding-top:38px;font-size:11px;color:var(--pink)}
.edition{position:absolute;left:792px;top:838px;font-size:11px;transform:rotate(-90deg);transform-origin:left top}
.logo{position:absolute;left:1008px;top:0;width:310px;height:192px;background:var(--logo-bg);display:flex;align-items:center;justify-content:center;gap:12px}
.logo__dot{width:46px;height:46px;border-radius:50%;background:var(--brown)}
.logo__name{font-family:"Open Sans",sans-serif;font-weight:700;font-size:22px;line-height:24px;color:var(--brown)}
.logo__name small{display:block;font-size:10px;line-height:14px}
.claim{position:absolute;left:1008px;top:636px;width:310px;height:254px;background:var(--logo-bg);border-radius:0 0 26px 26px;text-align:center;padding-top:62px;font-size:23px;line-height:29px;color:var(--brown)}
.heading{position:absolute;color:var(--brown);font-size:25px;line-height:32px}
</style>
</head>
<body>
<div class="stage">

  <!-- Außenseite -->
  <section class="sheet sheet--outer">
    <div class="band" style="left:0;top:192px;width:438px;height:698px;border-radius:0 30px 30px 0"></div>
    <div class="band" style="left:438px;top:192px;width:458px;height:698px;border-radius:30px 30px 30px 30px"></div>
    <div class="band" style="left:896px;top:0;width:452px;height:953px"></div>

    <div class="photo" role="img" aria-label="Foto: Frau mit braunem Hund im Wald" style="left:20px;top:0;width:395px;height:255px;border-radius:0 0 30px 30px;background:linear-gradient(135deg,#6f7a55,#9a6a3e 55%,#35435e)"></div>
    <div class="card" style="left:20px;top:255px;width:395px;height:605px">
      <span class="label">Workshops</span>
      Lorem ipsum dolor sit amet, consetetur sadipscing elitr, sed diam nonumy eirmod tempor invidunt ut labore et dolore magna aliquyam erat, sed diam voluptua. At vero eos et accusam et justo duo dolores et ea rebum.<br>
      Stet clita kasd gubergren, no sea takimata sanctus est Lorem ipsum dolor sit amet. Lorem ipsum dolor sit amet, consetetur sadipscing elitr, sed diam nonumy eirmod tempor invidunt.<br>
      Lorem ipsum dolor sit amet, consetetur sadipscing elitr, sed diam nonumy eirmod tempor invidunt ut labore et dolore magna aliquyam erat, sed diam voluptua. At vero eos et accusam et justo duo dolores et ea rebum.
    </div>
    <div class="offer" style="left:96px;top:636px;height:317px">
      <div class="offer__mark"></div>
      <div class="offer__title slab">Workshops</div>
      <div class="offer__sub">Kompaktes Training</div>
      <div class="offer__claim">Optimal für ein<br>effektives Training<br>in kurzer Zeit</div>
      <div class="offer__note">Für Hunde ab 10 Monaten</div>
    </div>

    <div class="portrait">Ihr Porträtfoto</div>
    <div class="card" style="left:470px;top:255px;width:394px;height:605px">
      <span class="label">Über mich</span>
      Lorem ipsum dolor sit amet, consetetur sadipscing elitr, sed diam nonumy eirmod tempor invidunt ut labore et dolore magna aliquyam erat, sed diam voluptua. At vero eos et accusam et justo duo dolores et ea rebum.<br>
      Inklusive Qualifikationen
    </div>
    <div class="heading slab" style="left:470px;top:602px;width:394px;text-align:center;font-size:22px">Kontakt</div>
    <div class="offer" style="left:543px;top:636px;height:317px">
      <div class="offer__mark"></div>
      <div class="contact__name slab">Pfotenwerk<br>Lindental</div>
      <div class="contact__lines">Name<br>Straße<br>Stadt<br>0151 000 12 34 5<br>Mail<br>web</div>
    </div>
    <div class="edition">10-2022</div>

    <div class="logo">
      <div class="logo__dot"></div>
      <div class="logo__name">PFOTENWERK<br>LINDENTAL<small>Hundetraining &amp; Verhaltensberatung</small></div>
    </div>
    <div class="photo" role="img" aria-label="Foto: Welpe läuft mit Spielzeug über eine Wiese" style="left:896px;top:192px;width:452px;height:444px;border-radius:30px 0 0 0;background:linear-gradient(160deg,#a9be5a,#7f9a3a 50%,#5d7a2b)"></div>
    <div class="claim slab">Ein fundiertes Training<br>ist der Schlüssel für<br>einen entspannten und<br>glücklichen Alltag.</div>
  </section>

  <!-- Innenseite -->
  <section class="sheet sheet--inner">
    <div class="heading slab" style="left:40px;top:108px">Fundiertes Training, Beratung<br>und Wissensvermittlung</div>
    <div class="band band--apricot" style="left:0;top:256px;width:452px;height:633px;border-radius:0 30px 30px 0"></div>
    <div class="card card--sand" style="left:21px;top:193px;width:401px;height:443px;padding-top:58px">
      Du möchtest, dass Dein Hund im Alltag zuverlässig ist und Du Dich auf ihn verlassen kannst? Spaß und ein Gefühl der Gemeinsamkeit sollen auch dabei sein?<br><br>
      At vero eos et accusam et justo duo dolores et ea rebum. Stet clita kasd gubergren, no sea takimata sanctus est Lorem ipsum dolor sit amet. Lorem ipsum dolor sit amet, consetetur sadipscing elitr, sed diam nonumy eirmod tempor invidunt ut labore et dolore magna aliquyam erat, sed diam voluptua.<br><br>
      Ich leite Dich im Training an, damit Du Deinen Hund anleiten kannst. Du wirst zum Fremdenführer für Deinen Hund. Wohlwollend und verständnisvoll zeigst Du ihm den Weg im alltäglichen Miteinander.
    </div>
    <div class="photo" role="img" aria-label="Foto: Frau kniet auf einer Wiese, Hund läuft auf sie zu" style="left:21px;top:637px;width:401px;height:317px;border-radius:30px 30px 0 0;background:linear-gradient(150deg,#5e6b3a,#a9a06a 55%,#4a8fc4)"></div>

    <div class="band" style="left:452px;top:193px;width:897px;height:696px;border-radius:30px 0 0 30px"></div>
    <div class="photo" role="img" aria-label="Foto: Welpe läuft im Abendlicht" style="left:475px;top:0;width:412px;height:255px;border-radius:0 0 30px 30px;background:linear-gradient(170deg,#c89a7c,#a46a45 60%,#5e3d2a)"></div>
    <div class="card" style="left:475px;top:257px;width:412px;height:603px;padding-top:58px">
      <span class="label">Einzeltraining</span>
      Lorem ipsum dolor sit amet, consetetur sadipscing elitr, sed diam nonumy eirmod tempor invidunt ut labore et dolore magna aliquyam erat, sed diam voluptua. At vero eos et accusam et justo duo dolores et ea rebum. Stet clita kasd gubergren, no sea takimata sanctus est Lorem ipsum dolor sit amet.<br>
      Lorem ipsum dolor sit amet, consetetur sadipscing elitr, sed diam nonumy eirmod tempor invidunt ut labore et dolore magna aliquyam erat, sed diam voluptua. At vero eos et accusam et justo duo dolores et ea rebum.<br>
      Stet clita kasd gubergren, no sea takimata sanctus est Lorem ipsum dolor sit amet. Lorem ipsum dolor sit amet, consetetur sadipscing elitr, sed diam.
    </div>
    <div class="heading slab" style="left:498px;top:270px">Vielfältige Trainingsangebote</div>
    <div class="offer" style="left:551px;top:637px;height:317px">
      <div class="offer__mark"></div>
      <div class="offer__title slab">Einzeltraining</div>
      <div class="offer__sub">1:1 Coaching</div>
      <div class="offer__claim">Optimal bei<br>Problemen oder als<br>exklusives Training</div>
      <div class="offer__note">Für Welpen, Junghunde<br>und erwachsene Hunde</div>
    </div>

    <div class="photo" role="img" aria-label="Foto: Gruppe angeleinter Hunde sitzt im Park" style="left:933px;top:0;width:394px;height:255px;border-radius:0 0 30px 30px;background:linear-gradient(160deg,#4f5a4a,#8a6a5e 55%,#a0574a)"></div>
    <div class="card" style="left:933px;top:257px;width:394px;height:603px;padding-top:58px">
      <span class="label">Gruppentraining</span>
      Lorem ipsum dolor sit amet, consetetur sadipscing elitr, sed diam nonumy eirmod tempor invidunt ut labore et dolore magna aliquyam erat, sed diam voluptua.<br>
      At vero eos et accusam et justo duo dolores et ea ebum. Stet clita kasd gubergren, no sea takimata sanctus est Lorem ipsum dolor sit amet. Lorem ipsum dolor sit amet, consetetur sadipscing elitr, sed diam nonumy eirmod tempor invidunt.<br>
      Lorem ipsum dolor sit amet, consetetur sadipscing elitr, sed diam nonumy eirmod tempor invidunt ut labore et dolore magna aliquyam erat, sed diam voluptua. At vero eos et accusam et justo duo dolores et ea rebum.
    </div>
    <div class="offer" style="left:1009px;top:637px;height:317px">
      <div class="offer__mark"></div>
      <div class="offer__title slab">Gruppentraining</div>
      <div class="offer__sub">Spaß in der Gruppe</div>
      <div class="offer__claim">Optimal für<br>Alltagstraining und<br>Beschäftigung</div>
      <div class="offer__note">Für Welpen, Junghunde<br>und erwachsene Hunde</div>
    </div>
  </section>

</div>
</body>
</html>
```